Biz Card & Stationary for Business Coaching Co.
Plan. Act. Grow.
Biz Card & Stationary for Business Coaching Co. - Consulting
Creative Brief
Simple
Marlow Quint
CEO
2864 38th Ave S Minneapolis, MN 55406
marlow@brightharbor.net
www.brightharbor.net
My office is home based so we don't need to use the physical address on the card.
I would like to use my logo or at least the logo symbol somehow on the back. Perhaps incorporate tag line "Plan. Act. Grow."

```html
<!DOCTYPE html>
<html lang="en">
<head>
<meta charset="utf-8">
<title>Bright Harbor Business Cards</title>
<link href="https://fonts.googleapis.com/css2?family=Montserrat:wght@500;700;800&family=Open+Sans:wght@400;600&display=swap" rel="stylesheet">
<style>
  :root {
    --backdrop: #6f6f71;
    --blue-deep: #1f3f8f;
    --blue-mid: #2f5cc0;
    --blue-light: #5a86de;
    --ink: #2a2f3a;
    --muted: #5b6270;
    --paper: #ffffff;
    --paper-shade: #eceef2;
  }
  * { margin: 0; padding: 0; box-sizing: border-box; }
  html, body { width: 1200px; height: 908px; overflow: hidden; }
  body {
    background: var(--backdrop);
    font-family: "Open Sans", sans-serif;
    position: relative;
  }
  .card {
    position: absolute;
    top: 309px;
    width: 500px;
    height: 290px;
    border-radius: 18px;
    overflow: hidden;
  }
  /* Front */
  .card-front {
    left: 70px;
    background: linear-gradient(125deg, var(--blue-deep) 0%, var(--blue-mid) 55%, var(--blue-light) 100%);
  }
  .symbol-area {
    position: absolute;
    right: 30px; top: 20px;
    width: 230px; height: 230px;
    border-radius: 50%;
    background: radial-gradient(circle, rgba(200,214,240,0.55) 0%, rgba(120,150,210,0.25) 55%, rgba(47,92,192,0) 75%);
  }
  .front-brand {
    position: absolute;
    left: 30px; bottom: 34px;
    color: var(--paper);
  }
  .wordmark {
    font-family: "Montserrat", sans-serif;
    font-weight: 800;
    font-size: 30px;
    letter-spacing: 0.5px;
    line-height: 1;
  }
  .tagline {
    font-family: "Montserrat", sans-serif;
    font-weight: 500;
    font-size: 10.5px;
    letter-spacing: 1.6px;
    margin-top: 6px;
    text-transform: uppercase;
  }
  /* Back */
  .card-back {
    left: 630px;
    background: linear-gradient(180deg, var(--paper) 0%, var(--paper-shade) 100%);
  }
  .back-swoosh { position: absolute; left: 0; bottom: 0; width: 500px; height: 110px; }
  .back-logo {
    position: absolute;
    left: 30px; top: 92px;
    display: flex; align-items: center; gap: 10px;
  }
  .logo-dot {
    width: 30px; height: 30px; border-radius: 50%;
    background: var(--blue-deep);
  }
  .back-logo .wordmark { color: var(--blue-deep); font-size: 24px; }
  .back-logo .tagline { color: var(--blue-deep); font-size: 8px; letter-spacing: 1.2px; margin-top: 4px; }
  .contact {
    position: absolute;
    left: 300px; top: 34px;
    padding-left: 16px;
    border-left: 1px solid #d5d9e0;
    height: 150px;
  }
  .person-name {
    font-family: "Montserrat", sans-serif;
    font-weight: 700;
    font-size: 14px;
    color: var(--blue-mid);
  }
  .person-role {
    font-size: 10px; font-weight: 600; color: var(--ink);
    margin-bottom: 16px;
  }
  .contact-line {
    font-size: 10px; color: var(--muted); line-height: 1.5;
    display: flex; align-items: center; gap: 6px;
  }
  .contact-line svg { width: 11px; height: 11px; flex: none; }
  .address { margin-bottom: 4px; display: block; }
  .website {
    position: absolute;
    right: 34px; bottom: 18px;
    color: var(--paper);
    font-family: "Montserrat", sans-serif;
    font-weight: 700;
    font-size: 12px;
    letter-spacing: 2px;
  }
</style>
</head>
<body>
  <section class="card card-front" aria-label="Card front">
    <div class="symbol-area" role="img" aria-label="Area for the brand symbol"></div>
    <div class="front-brand">
      <div class="wordmark">BRIGHT HARBOR</div>
      <div class="tagline">Business Coaching and Consulting</div>
    </div>
  </section>

  <section class="card card-back" aria-label="Card back">
    <svg class="back-swoosh" viewBox="0 0 500 110" preserveAspectRatio="none" aria-hidden="true">
      <defs>
        <linearGradient id="swooshFill" x1="0" y1="0" x2="1" y2="0">
          <stop offset="0" stop-color="#5a86de"/>
          <stop offset="1" stop-color="#1f3f8f"/>
        </linearGradient>
      </defs>
      <path d="M0 110 C 160 100, 330 80, 500 20 L500 110 Z" fill="#c7ccd6"/>
      <path d="M60 110 C 220 100, 360 85, 500 36 L500 110 Z" fill="url(#swooshFill)"/>
    </svg>
    <div class="back-logo">
      <div class="logo-dot"></div>
      <div>
        <div class="wordmark">BRIGHT HARBOR</div>
        <div class="tagline">Business Coaching and Consulting</div>
      </div>
    </div>
    <div class="contact">
      <div class="person-name">Marlow Quint</div>
      <div class="person-role">CEO</div>
      <div class="contact-line address">2864 38th Ave S<br>Minneapolis, MN 55406</div>
      <div class="contact-line">
        <svg viewBox="0 0 12 12"><circle cx="6" cy="6" r="5.5" fill="none" stroke="#2f5cc0"/><path d="M4 3.5 L5 3.5 L5.5 5 L4.8 5.6 Q5.6 7 6.8 7.4 L7.4 6.6 L8.6 7.2 L8.6 8.2 Q5 8.5 3.6 4.2 Z" fill="#2f5cc0"/></svg>
        612.555.0147
      </div>
      <div class="contact-line">
        <svg viewBox="0 0 12 12"><circle cx="6" cy="6" r="5.5" fill="none" stroke="#2f5cc0"/><rect x="3" y="4" width="6" height="4" fill="none" stroke="#2f5cc0" stroke-width="0.8"/><path d="M3 4 L6 6.3 L9 4" fill="none" stroke="#2f5cc0" stroke-width="0.8"/></svg>
        marlow@brightharbor.net
      </div>
    </div>
    <div class="website">www.brightharbor.net</div>
  </section>
</body>
</html>
```